Verantix - Solution provider in business consulting

Verantix is a swiss based company providing solutions for developing markets. The business covers various fields of business consulting, such as supply chain, product costs, quality management and manufacturing management. The Business operates in a efficient, straight and solution oriented manner.
The final design should communicate these characteristics. Asian people as well as as western people shall identify the qualities of the company at first sight.
The customer needs business cards with a simple view but an recognizable design, printed in high quality. Engraved elements such as the globe or simple words are possible.
Available colors are: (RAL)
102/102/102
51/102/102
153/204/153
255/102/51
Font: Calibri
Industry/Entity Type
Business
Look and feel
Each slider illustrates characteristics of the customer's brand and the style your logo design should communicate.

```html
<!DOCTYPE html>
<html lang="en">
<head>
<meta charset="utf-8">
<title>Verantix business card</title>
<link rel="stylesheet" href="https://fonts.googleapis.com/css2?family=Carlito:wght@400;700&display=swap">
<style>
  :root {
    --page-bg: #d9d6d1;
    --card-dark: #666666;
    --card-dark-edge: #5a5a5a;
    --card-light: #ededed;
    --globe-light: #f7f7f7;
    --globe-shade: #cfcfcf;
    --ink: #6b6b6b;
    --ink-strong: #555555;
    --white: #ffffff;
  }
  * { box-sizing: border-box; margin: 0; padding: 0; }
  html, body {
    width: 1200px; height: 1022px; overflow: hidden;
    background: var(--page-bg);
    font-family: "Carlito", "Calibri", sans-serif;
  }
  .sheet {
    width: 1200px; height: 1022px;
    display: flex; flex-direction: column;
    align-items: center; justify-content: center; gap: 60px;
  }
  .card {
    position: relative;
    width: 700px; height: 400px;
    border-radius: 18px;
    overflow: hidden;
    box-shadow: 0 10px 30px rgba(0,0,0,0.22);
  }
  .card-front {
    background: var(--card-dark);
    display: flex; align-items: center; justify-content: center;
  }
  .wordmark {
    display: flex; align-items: center; gap: 16px;
    color: var(--white);
    font-size: 78px; font-weight: 400; letter-spacing: 1px;
  }
  .wordmark-dot {
    width: 26px; height: 26px; border-radius: 50%;
    background: var(--white);
  }
  .card-back { background: var(--card-dark); }
  .card-back .art { position: absolute; inset: 0; }
  .contact {
    position: absolute; left: 46px; top: 120px;
    color: var(--ink);
  }
  .contact-name {
    font-size: 30px; font-weight: 700; color: var(--ink-strong);
    line-height: 1.05;
  }
  .contact-role { font-size: 17px; margin-bottom: 20px; }
  .contact-address { font-size: 17px; line-height: 1.3; margin-bottom: 12px; }
  .contact-list { list-style: none; font-size: 17px; line-height: 1.35; }
  .contact-list li { display: flex; align-items: center; gap: 10px; }
  .contact-list svg { width: 14px; height: 14px; fill: var(--ink); flex: none; }
</style>
</head>
<body>
<main class="sheet">
  <section class="card card-front" aria-label="Card front">
    <div class="wordmark"><span>verantix</span><span class="wordmark-dot"></span></div>
  </section>

  <section class="card card-back" aria-label="Card back">
    <svg class="art" viewBox="0 0 700 400" width="700" height="400">
      <defs>
        <radialGradient id="globeFill" cx="0.4" cy="0.4" r="0.7">
          <stop offset="0" stop-color="var(--globe-light)"/>
          <stop offset="1" stop-color="var(--globe-shade)"/>
        </radialGradient>
      </defs>
      <path class="light-panel" d="M0 0 H300 C300 110 340 170 420 200 L420 400 H0 Z" fill="var(--card-light)"/>
      <circle class="globe-disc" cx="430" cy="310" r="230" fill="var(--card-light)"/>
      <circle class="globe-map" cx="430" cy="310" r="215" fill="url(#globeFill)" role="img" aria-label="Faint world map globe decoration"/>
    </svg>
    <div class="contact">
      <p class="contact-name">Lukas Brenner</p>
      <p class="contact-role">CEO</p>
      <p class="contact-address">Verantix GmbH Lindenweg 14<br>8400 Winterthur Switzerland</p>
      <ul class="contact-list">
        <li><svg viewBox="0 0 14 14"><path d="M3 0h8a1 1 0 0 1 1 1v12a1 1 0 0 1-1 1H3a1 1 0 0 1-1-1V1a1 1 0 0 1 1-1zm1 2v8h6V2z"/></svg>+41 79 555 0142</li>
        <li><svg viewBox="0 0 14 14"><path d="M3 1l2.5 3-1.5 1.5c.8 1.8 2.2 3.2 4 4L9.5 8l3 2.5-1.5 2.5C6 12.5 1.5 8 1 2.5z"/></svg>+41 71 555 0187</li>
        <li><svg viewBox="0 0 14 14"><path d="M1 3h12v8H1zm1 1v.4l5 3.3 5-3.3V4zm0 1.6V10h10V5.6L7 9z"/></svg>lukas.brenner@verantix.ch</li>
        <li><svg viewBox="0 0 14 14"><path d="M7 1a6 6 0 1 0 0 12A6 6 0 0 0 7 1zm0 1.2c.7.8 1.2 2 1.4 3.3H5.6C5.8 4.2 6.3 3 7 2.2zM2.3 6.5h2.2c0 .4 0 .7.1 1H2.3a4.8 4.8 0 0 1 0-1zm3.3 2h2.8C8.2 9.8 7.7 11 7 11.8 6.3 11 5.8 9.8 5.6 8.5zm4-2h2.1a4.8 4.8 0 0 1 0 1H9.5c.1-.3.1-.6.1-1z"/></svg>www.verantix.ch</li>
      </ul>
    </div>
  </section>
</main>
</body>
</html>
```